Orthodontic Office Needs New Stationary

We have recently renovated our office and are opening a second location. We need new stationary/branding to go with our new look. We like our logo, but are open to changing the colors to match the office look/feel more.

```html
<!DOCTYPE html>
<html lang="en">
<head>
<meta charset="utf-8">
<title>Marlow &amp; Finch Orthodontics – Stationery</title>
<link href="https://fonts.googleapis.com/css2?family=Questrial&family=Open+Sans:wght@400;600;700&display=swap" rel="stylesheet">
<style>
  :root {
    --bg: #c8cbce;
    --paper: #ffffff;
    --orange: #f0962a;
    --blue: #2b9cc9;
    --ink: #555a5e;
    --dark: #222;
    --flap: #dcdddf;
    --shadow: 0 2px 4px rgba(0,0,0,.25);
  }
  * { box-sizing: border-box; margin: 0; padding: 0; }
  html, body { width: 1200px; height: 754px; overflow: hidden; }
  body { background: var(--bg); font-family: "Questrial", sans-serif; color: var(--ink); position: relative; }

  .sheet { position: absolute; background: var(--paper); box-shadow: var(--shadow); overflow: hidden; }
  .wordmark { font-family: "Questrial", sans-serif; color: var(--orange); white-space: nowrap; text-transform: uppercase; display: inline-block; text-align: center; line-height: 1.1; letter-spacing: .03em; }
  .wordmark > span { display: block; }
  .rule { position: absolute; height: 1px; background: var(--blue); }

  /* merchandise tiles */
  .merch { position: absolute; background: var(--paper); box-shadow: var(--shadow); display: flex; align-items: center; justify-content: center; }
  .merch-cap { left: 137px; top: 72px; width: 54px; height: 50px; border-radius: 24px 24px 4px 4px; }
  .merch-cap .wordmark { font-size: 4px; }
  .merch-shirt { left: 92px; top: 137px; width: 146px; height: 170px; border-radius: 6px; align-items: flex-start; justify-content: flex-end; padding: 50px 24px 0 0; }
  .merch-shirt .wordmark { font-size: 4px; }
  .merch-shirt .hem { position: absolute; left: 0; right: 0; bottom: 0; height: 18px; background: var(--orange); }
  .merch-shirt .trim { position: absolute; top: 60px; width: 10px; height: 6px; background: var(--blue); }
  .merch-shirt .trim.left { left: 0; } .merch-shirt .trim.right { right: 0; }
  .merch-mug { left: 105px; top: 351px; width: 117px; height: 132px; border-radius: 4px 4px 12px 12px; }
  .merch-mug .wordmark { font-size: 8.5px; }
  .merch-bag { left: 108px; top: 556px; width: 122px; height: 130px; }
  .merch-bag .wordmark { font-size: 7.5px; }

  /* business card front */
  .card-front { left: 283px; top: 72px; width: 367px; height: 94px; }
  .card-front .rule { left: 0; top: 47px; width: 14px; }
  .card-front .wordmark { position: absolute; left: 18px; top: 36px; font-size: 9.5px; }
  .contact { position: absolute; left: 129px; top: 21px; }
  .contact .name { font-size: 8.5px; color: var(--orange); font-weight: 700; }
  .contact .role { font-size: 5px; color: var(--blue); margin-bottom: 6px; }
  .contact li { list-style: none; font-size: 6.3px; line-height: 9.5px; display: flex; align-items: center; gap: 4px; }
  .ico { width: 5px; height: 5px; border-radius: 50%; background: var(--blue); display: inline-block; flex: none; }

  /* card back */
  .card-back { left: 283px; top: 187px; width: 157px; height: 94px; }
  .card-back .rule { left: 0; right: 0; top: 46px; }
  .card-back .wordmark { position: absolute; left: 50%; top: 38px; transform: translateX(-50%); background: var(--paper); padding: 0 5px; font-size: 7.5px; }

  /* vertical card */
  .card-alt { left: 493px; top: 189px; width: 158px; height: 95px; text-align: center; }
  .card-alt .brand { position: absolute; left: 0; right: 0; top: 16px; }
  .card-alt .wordmark { font-size: 7.5px; }
  .card-alt .rule { left: 0; right: 0; top: 47px; }
  .card-alt .tag { position: absolute; left: 55px; top: 41px; width: 48px; height: 12px; background: var(--paper); border: .6px solid var(--blue); font-size: 4.5px; color: var(--orange); line-height: 6px; padding-top: 1px; }
  .card-alt .tag small { display: block; font-size: 2.5px; line-height: 3px; color: var(--blue); }
  .card-alt .lines { position: absolute; left: 0; right: 0; top: 57px; font-size: 3.8px; line-height: 9.6px; }

  /* compliment slip */
  .slip { left: 283px; top: 300px; width: 367px; height: 185px; }
  .slip .wordmark { position: absolute; left: 12px; top: 11px; font-size: 9px; text-align: left; }
  .slip .addr { position: absolute; left: 12px; top: 30px; font-size: 5px; }

  /* envelope */
  .envelope { left: 283px; top: 504px; width: 367px; height: 184px; }
  .envelope .flap { position: absolute; left: 0; top: 0; width: 100%; height: 51px; background: var(--flap); border-radius: 0 0 20px 20px; display: flex; align-items: center; justify-content: center; }
  .envelope .wordmark { font-size: 11px; }

  /* letterhead */
  .letterhead { left: 683px; top: 69px; width: 443px; height: 622px; font-family: "Open Sans", sans-serif; }
  .letterhead .rule.top { left: 0; top: 58px; width: 36px; }
  .letterhead .brand { position: absolute; left: 42px; top: 44px; font-size: 12.5px; }
  .sender { position: absolute; left: 40px; top: 142px; }
  .sender .name { color: var(--orange); font-size: 8px; font-weight: 600; }
  .sender .role { color: var(--dark); font-size: 6px; margin-top: 2px; }
  .date { position: absolute; right: 45px; top: 164px; font-size: 7.5px; }
  .body { position: absolute; left: 40px; top: 203px; width: 365px; font-size: 7.3px; line-height: 15.5px; }
  .body p { margin-bottom: 15.5px; white-space: nowrap; overflow: hidden; }
  .signature { position: absolute; right: 45px; top: 472px; width: 62px; height: 22px; background: linear-gradient(90deg, #f3f3f3, #e6e6e6); }
  .signer { position: absolute; left: 336px; top: 495px; font-size: 7px; color: var(--dark); line-height: 8.5px; }
  .footer { position: absolute; left: 33px; top: 584px; width: 377px; height: 15px; border: .7px solid var(--blue); display: flex; align-items: center; gap: 8px; padding-left: 4px; font-family: "Questrial", sans-serif; font-size: 9.5px; }
  .footer span { display: flex; align-items: center; gap: 3px; }
  .footer .ico { width: 7px; height: 7px; }
  .letterhead .rule.bottom { left: 410px; top: 591px; width: 33px; }
</style>
</head>
<body>

  <div class="merch merch-cap"><span class="wordmark"><span>Marlow &amp; Finch</span><span>Orthodontics</span></span></div>
  <div class="merch merch-shirt">
    <span class="wordmark"><span>Marlow &amp; Finch</span><span>Orthodontics</span></span>
    <span class="trim left"></span><span class="trim right"></span>
    <span class="hem"></span>
  </div>
  <div class="merch merch-mug"><span class="wordmark"><span>Marlow &amp; Finch</span><span>Orthodontics</span></span></div>
  <div class="merch merch-bag"><span class="wordmark"><span>Marlow &amp; Finch</span><span>Orthodontics</span></span></div>

  <section class="sheet card-front">
    <span class="rule"></span>
    <span class="wordmark"><span>Marlow &amp; Finch</span><span>Orthodontics</span></span>
    <div class="contact">
      <p class="name">JOHN DOE</p>
      <p class="role">Mangaer</p>
      <ul>
        <li><i class="ico"></i>111-222-333</li>
        <li><i class="ico"></i>info@marlowfinch.com</li>
        <li><i class="ico"></i>Your address, your city, box 88900</li>
      </ul>
    </div>
  </section>

  <section class="sheet card-back">
    <span class="rule"></span>
    <span class="wordmark"><span>Marlow &amp; Finch</span><span>Orthodontics</span></span>
  </section>

  <section class="sheet card-alt">
    <div class="brand"><span class="wordmark"><span>Marlow &amp; Finch</span><span>Orthodontics</span></span></div>
    <span class="rule"></span>
    <div class="tag">JOHN DOE<small>Mangaer</small></div>
    <div class="lines">111-222-333<br>info@marlowfinch.com<br>Your address, your city, box 88900</div>
  </section>

  <section class="sheet slip">
    <span class="wordmark"><span>Marlow &amp; Finch</span><span>Orthodontics</span></span>
    <p class="addr">Your address, your city, box 88900</p>
  </section>

  <section class="sheet envelope">
    <div class="flap"><span class="wordmark"><span>Marlow &amp; Finch</span><span>Orthodontics</span></span></div>
  </section>

  <section class="sheet letterhead">
    <span class="rule top"></span>
    <span class="wordmark brand"><span>Marlow &amp; Finch</span><span>Orthodontics</span></span>
    <div class="sender">
      <p class="name">John Doe</p>
      <p class="role">Chief Director</p>
    </div>
    <p class="date">Date, 00 September, 2021</p>
    <div class="body">
      <p>This is a sample letter that has been placed to demonstrate typing remat (Your Company). letterhead<br>design. When positioned properly, it will serve to work in harmony with all other elements letterhead.<br>This letterhead design is meant to project an image</p>
      <p>This letterhead design is meant project an image of professionalism reliability. By using simple aligen<br>we have created a very spacious feeling. The simplicity suggest rengththe spaciousnes contributes h<br>aesthetics the layout. These basic qualities along with the (Your Company)</p>
      <p>look and helps reinforce the (Your Company) brand. letterhead design is meant to project an image p<br>design. When positioned properly, it will serve to work in harmony all the other elements letterhead.<br>sionalism and reliability.</p>
      <p>This letterhead design is based on the (Form of your logo) form (Your Company) logo. Each stationery<br>we have created a very spacious feeling. The simplicity suggests strength the spaciousnes contribute<br>part of the (Form of your logo).</p>
    </div>
    <div class="signature" role="img" aria-label="Handwritten signature of John Doe"></div>
    <p class="signer"><b>John Doe</b><br>Manager</p>
    <div class="footer">
      <span><i class="ico"></i>111-222-333</span>
      <span><i class="ico"></i>info@marlowfinch.com</span>
      <span><i class="ico"></i>Your address, your city, box 88900</span>
    </div>
    <span class="rule bottom"></span>
  </section>

</body>
</html>
```